Lantern Walk! A website showcasing who I am as a person

Lantern Walk started out as idea for me to better myself as a person and work on small projects that would help me grow as a person. Now I want to build a website showcasing "Lantern Walk." I want the website to showcase who I am and how I have grown both professionally and personally. I can build the raw code of the website on my own but I am not really much of a designer. I am looking for a design where I can write and post blogs, articles and share my thoughts. A little about myself and the ideas and interests that I want to share
What is Lantern Walk
Who I am
Background - Professional
Brand Marketing
Email Automation
Hiking
Rock Climbing
Traveling
Exercising and Transformation
"Personal Thoughts"
Hopefully this is enough information to get people started on some designs.
Industry/Entity Type
Work
Number of Pages Required
3 page

```html
<!DOCTYPE html>
<html lang="en">
<head>
<meta charset="utf-8">
<title>Lantern Walk</title>
<link rel="stylesheet" href="https://fonts.googleapis.com/css2?family=Jost:wght@400;500;600&family=Libre+Baskerville&display=swap">
<style>
  :root {
    --slate: #58595c;
    --slate-soft: #5f6063;
    --blue: #27a7e3;
    --blue-soft: #3aafe6;
    --blue-line: #4fb8ec;
    --mist: #d9d9d9;
    --ink: #1e1e1e;
    --paper: #ffffff;
    --contact: #6d6e70;
    --field: #959698;
    --soft-text: #d6d7d9;
  }
  html, body { margin: 0; padding: 0; }
  body {
    width: 1200px; height: 3727px; overflow: hidden; position: relative;
    background: var(--paper); font-family: "Jost", sans-serif; color: var(--ink);
  }
  .abs { position: absolute; }
  p { margin: 0; }

  /* Hero */
  .hero { left: 0; top: 0; width: 1200px; height: 812px; background: var(--slate); overflow: hidden; }
  .hero-texture { background: var(--slate-soft); }
  .hero-title { left: 161px; top: 166px; margin: 0; font-weight: 400; font-size: 64px; color: var(--paper); letter-spacing: 1px; }
  .hero-lead { left: 203px; top: 282px; width: 440px; font-size: 31px; line-height: 36px; color: var(--soft-text); }
  .hero-button { left: 407px; top: 400px; width: 207px; height: 37px; background: var(--paper); color: var(--ink);
    font-size: 20px; line-height: 37px; text-align: center; text-decoration: none; }
  .menu-icon { left: 937px; top: 179px; width: 40px; height: 26px; }
  .menu-icon span { display: block; height: 5px; background: var(--paper); margin-bottom: 5px; }

  /* About */
  .about-shape { left: 0; top: 812px; }
  .section-heading-light { left: 94px; top: 882px; width: 420px; margin: 0; text-align: center; font-weight: 500; font-size: 35px; color: var(--paper); }
  .about-text { left: 94px; top: 966px; width: 405px; font-size: 17px; line-height: 22.7px; }
  .avatar { left: 209px; top: 1250px; width: 188px; height: 188px; border-radius: 50%; background: #c9c9c9; border: 4px solid var(--paper); box-sizing: border-box; }
  .pro-heading { left: 723px; top: 875px; width: 321px; height: 47px; margin: 0; background: var(--blue); color: var(--paper);
    font-weight: 500; font-size: 33px; line-height: 47px; text-align: center; }
  .pro-text { left: 700px; top: 966px; width: 405px; font-size: 17px; line-height: 22.7px; }

  /* Exercising */
  .exercise-band { left: 0; top: 1520px; width: 1200px; height: 301px; background: var(--mist); }
  .exercise-frame { left: 638px; top: 1471px; width: 473px; height: 99px; border: 1.5px solid var(--blue-line); box-sizing: border-box; }
  .exercise-heading { left: 629px; top: 1493px; width: 457px; height: 50px; margin: 0; background: var(--slate); color: var(--paper);
    font-weight: 400; font-size: 33px; line-height: 50px; text-align: center; }
  .exercise-text { left: 94px; top: 1613px; width: 700px; font-size: 24px; line-height: 32.5px; }

  /* Interests */
  .photo-hiking { left: 614px; top: 1988px; width: 489px; height: 327px; background: linear-gradient(180deg, #a9a9a9, #d4d4d4 45%, #5e5e5e); }
  .photo-climbing { left: 104px; top: 2234px; width: 510px; height: 318px; background: linear-gradient(180deg, #8e8e8e, #cfcfcf 70%, #4a4a4a); }
  .photo-travel { left: 614px; top: 2492px; width: 494px; height: 320px; background: linear-gradient(135deg, #e2e2e2, #a6a6a6); }
  .tag { background: var(--blue); color: var(--paper); font-weight: 600; font-size: 18px; text-align: center; text-decoration: none; }
  .tag-name { height: 30px; line-height: 30px; }
  .tag-more { height: 32px; line-height: 32px; }

  /* Blog band */
  .blog-band { left: 0; top: 2852px; width: 1200px; height: 460px;
    background: linear-gradient(100deg, var(--blue) 0%, var(--blue-soft) 50%, var(--blue) 100%); }
  .blog-text { left: 442px; top: 2945px; width: 350px; font-weight: 600; font-size: 22.5px; line-height: 32px; color: var(--paper); }
  .blog-frame { left: 450px; top: 3143px; width: 330px; height: 87px; border: 1.5px solid var(--paper); box-sizing: border-box; }
  .blog-button { left: 427px; top: 3163px; width: 373px; height: 57px; background: var(--slate); color: var(--paper);
    font-family: "Libre Baskerville", serif; font-size: 23px; line-height: 57px; text-align: center; text-decoration: none; }

  /* Contact */
  .contact { left: 0; top: 3312px; width: 1200px; height: 415px; background: var(--contact); }
  .contact-heading { left: 229px; top: 3386px; margin: 0; font-weight: 500; font-size: 29px; color: var(--paper); }
  .contact-intro { left: 229px; top: 3447px; width: 330px; font-size: 16px; line-height: 25px; font-weight: 500; color: var(--paper); }
  .contact-line { left: 229px; font-size: 16px; font-weight: 500; color: var(--paper); }
  .social { top: 3683px; font-size: 17px; font-weight: 500; color: var(--paper); text-decoration: none; }
  .field { left: 763px; width: 310px; background: var(--field); color: var(--paper); font-size: 16px; padding: 4px 6px; box-sizing: border-box; }
  .send { left: 979px; top: 3665px; width: 94px; height: 37px; background: var(--blue); color: var(--paper);
    font-size: 28px; line-height: 37px; text-align: center; }
</style>
</head>
<body>

<header class="abs hero">
  <div class="abs hero-texture" style="left:560px;top:0;width:280px;height:150px;" role="img" aria-label="Dot pattern texture"></div>
  <div class="abs hero-texture" style="left:0;top:410px;width:235px;height:340px;" role="img" aria-label="Dot pattern texture"></div>
  <div class="abs hero-texture" style="left:1006px;top:0;width:194px;height:807px;" role="img" aria-label="Outline of a rock climber on a cliff edge"></div>
  <div class="abs hero-texture" style="left:830px;top:320px;width:176px;height:300px;" role="img" aria-label="Decorative circle ornament"></div>
  <div class="abs hero-texture" style="left:55px;top:676px;width:802px;height:74px;" role="img" aria-label="Decorative line ornament"></div>
  <h1 class="abs hero-title">Lantern Walk</h1>
  <p class="abs hero-lead">Lorem ipsum dolor sit amet consectetur adipiscing elit.</p>
  <a class="abs hero-button" href="#about">Find out more</a>
  <nav class="abs menu-icon" aria-label="Menu"><span></span><span></span><span></span></nav>
</header>

<section id="about">
  <svg class="abs about-shape" width="725" height="522" viewBox="0 0 725 522" aria-hidden="true">
    <polygon points="0,0 725,0 509,522 0,522" fill="var(--blue)"/>
  </svg>
  <h2 class="abs section-heading-light">Who Am I</h2>
  <p class="abs about-text">Sed ut perspiciatis unde omnis iste natus error sit voluptatem accusantium doloremque laudantium, totam rem aperiam, eaque ipsa quae ab illo inventore veritatis et quasi architecto beatae vitae dicta sunt explicabo. Nemo enim ipsam voluptatem quia voluptas sit aspernatur aut odit aut fugit, sed quia consequuntur magni dolores eos qui ratione voluptatem sequi nesciunt. Neque porro quisquam est, qui dolorem ipsum quia dolor sit amet, consectetur, adipisci velit.</p>
  <div class="abs avatar" role="img" aria-label="Profile portrait"></div>

  <h2 class="abs pro-heading">Professional</h2>
  <p class="abs pro-text">"Sed ut perspiciatis unde omnis iste natus error sit voluptatem accusantium doloremque laudantium, totam rem aperiam, eaque ipsa quae ab illo inventore veritatis et quasi architecto beatae vitae dicta sunt explicabo. Nemo enim ipsam voluptatem quia voluptas sit aspernatur aut odit aut fugit, sed quia consequuntur magni dolores eos qui ratione voluptatem sequi nesciunt. Neque porro quisquam est, qui dolorem ipsum quia dolor sit amet, consectetur, adipisci velit</p>
</section>

<section>
  <div class="abs exercise-band"></div>
  <div class="abs exercise-frame"></div>
  <h2 class="abs exercise-heading">Exercising and Transformation</h2>
  <p class="abs exercise-text">Lorem ipsum dolor sit amet, consectetur adipiscing elit, sed do eiusmod tempor incididunt ut labore et dolore magna aliqua. Ut enim ad minim veniam, quis nostrud exercitation ullamco laboris nisi ut aliquip ex ea commodo consequat. Duis aute irure dolor in reprehenderit in voluptate velit esse cillum dolore eu fugiat nulla pariatur.</p>
</section>

<section>
  <div class="abs photo-hiking" role="img" aria-label="Hiker with backpack beside a mountain lake"></div>
  <div class="abs photo-climbing" role="img" aria-label="Climber on a rock face at sunset"></div>
  <div class="abs photo-travel" role="img" aria-label="Map on a table with cameras and coffee cups"></div>

  <span class="abs tag tag-name" style="left:529px;top:2099px;width:154px;">HIKING</span>
  <a class="abs tag tag-more" href="#" style="left:509px;top:2169px;width:169px;">LEARN MORE</a>
  <span class="abs tag tag-name" style="left:497px;top:2373px;width:201px;">ROCK CLIMBING</span>
  <a class="abs tag tag-more" href="#" style="left:517px;top:2427px;width:169px;">LEARN MORE</a>
  <span class="abs tag tag-name" style="left:539px;top:2631px;width:144px;">TRAVELING</span>
  <a class="abs tag tag-more" href="#" style="left:529px;top:2691px;width:174px;">LEARN MORE</a>
</section>

<section>
  <div class="abs blog-band" role="img" aria-label="Blue band with light line texture"></div>
  <p class="abs blog-text">Lorem ipsum dolor sit amet, consectetur adipiscing elit, sed do eiusmod tempor incididunt ut labore et dolore magna aliqua.</p>
  <div class="abs blog-frame"></div>
  <a class="abs blog-button" href="#">MY THOUGHTS/BLOG</a>
</section>

<footer>
  <div class="abs contact"></div>
  <h2 class="abs contact-heading">CONTACT</h2>
  <p class="abs contact-intro">Here you can contact me through email, phone number and other social media sites.</p>
  <p class="abs contact-line" style="top:3582px;">EMAIL: hello@lanternwalk.net</p>
  <p class="abs contact-line" style="top:3634px;">Phone: +55990 4408</p>
  <a class="abs social" href="#" style="left:232px;">Chirper</a>
  <a class="abs social" href="#" style="left:318px;">Friendbook</a>

  <form>
    <div class="abs field" style="top:3384px;height:40px;">Name</div>
    <div class="abs field" style="top:3441px;height:40px;">Email</div>
    <div class="abs field" style="top:3496px;height:40px;">Subject</div>
    <div class="abs field" style="top:3558px;height:89px;">Message</div>
    <div class="abs send">Send</div>
  </form>
</footer>

</body>
</html>
```